Asphalt Driveway Billboard Design

We need a billboard designed for an Asphalt & Concrete Company in Minnesota. We want to advertise Asphalt Driveways on this billboard! Logo is uploaded below. Our website is tamlin-paving.com for more information.

```html
<!DOCTYPE html>
<html lang="en">
<head>
<meta charset="utf-8">
<title>Tamlin Asphalt &amp; Concrete Billboard</title>
<link href="https://fonts.googleapis.com/css2?family=Poppins:ital,wght@0,400;0,500;0,600;0,700;1,700;1,800&display=swap" rel="stylesheet">
<style>
  :root {
    --navy: #2a1f9e;
    --orange: #f26a0d;
    --charcoal: #3a3a3c;
    --grey-text: #555558;
    --cyan: #2fc6e8;
    --page: #e6e6e6;
    --white: #ffffff;
  }
  * { margin: 0; padding: 0; box-sizing: border-box; }
  html, body { width: 1200px; height: 1017px; overflow: hidden; background: var(--page); }
  body { position: relative; font-family: "Poppins", sans-serif; }

  .billboard {
    position: absolute; left: 30px; top: 346px;
    width: 1140px; height: 325px;
    background: var(--white); overflow: hidden;
  }
  .billboard-shapes { position: absolute; inset: 0; width: 100%; height: 100%; }

  .brand { position: absolute; left: 62px; top: 78px; color: var(--charcoal); font-weight: 700; text-align: center; }
  .brand-mark { width: 38px; height: 38px; background: var(--navy); margin: 0 auto 8px; }
  .brand-name { font-size: 30px; line-height: 1; letter-spacing: 1px; }
  .brand-sub { font-size: 9px; letter-spacing: 1px; margin-top: 4px; }

  .headline { position: absolute; left: 300px; top: 62px; transform: rotate(-2.4deg); transform-origin: left bottom; }
  .tagline { font-size: 15px; font-weight: 700; font-style: italic; color: var(--navy); letter-spacing: 9.2px; white-space: nowrap; margin-left: 10px; }
  .title { font-size: 46px; font-weight: 800; font-style: italic; color: var(--navy); white-space: nowrap; line-height: 1; letter-spacing: 0.5px; }
  .title .accent { color: var(--orange); }

  .services { position: absolute; top: 220px; display: flex; flex-direction: column; transform: rotate(-1.8deg); transform-origin: left top; }
  .services li { list-style: none; color: var(--white); font-weight: 600; font-size: 15px; line-height: 14.5px; white-space: nowrap; display: flex; align-items: center; gap: 5px; }
  .tick { width: 8px; height: 8px; flex: none; }
  .services.col-1 { left: 84px; top: 222px; }
  .services.col-2 { left: 313px; top: 216px; }
  .services.col-3 { left: 493px; top: 208px; }

  .contact { position: absolute; left: 792px; top: 243px; }
  .contact-label { font-size: 11px; color: var(--grey-text); font-weight: 500; margin-left: 18px; letter-spacing: 0.3px; }
  .contact-row { display: flex; align-items: center; gap: 10px; }
  .phone { font-size: 31px; font-weight: 800; font-style: italic; color: var(--navy); line-height: 1.05; letter-spacing: 0.5px; }
  .web { font-size: 18px; font-weight: 500; color: var(--grey-text); letter-spacing: 2.6px; line-height: 1; }
  .icon { width: 15px; height: 15px; flex: none; }

  .partners { position: absolute; left: 282px; top: 292px; display: flex; align-items: center; gap: 18px; }
  .badge { height: 14px; border-radius: 3px; }
  .badge.listing { width: 100px; background: #f0a060; }
  .badge.association { width: 52px; background: #8c9bc2; }
  .badge.institute { width: 96px; background: #9aa0a8; }
  .badge.rating { width: 46px; background: #2f6fb5; }
  .badge.review { width: 22px; background: #e2463a; }
</style>
</head>
<body>
  <div class="billboard">
    <svg class="billboard-shapes" viewBox="0 0 1967 560" preserveAspectRatio="none" aria-hidden="true">
      <polygon points="0,350 1967,260 1967,560 0,560" fill="var(--navy)"/>
      <path d="M1967,375 L1280,380 C1240,381 1215,400 1210,440 L1206,452 C1200,470 1186,475 1168,476 L392,486 C362,487 343,505 343,530 L343,560 L1967,560 Z" fill="var(--white)"/>
      <line x1="520" y1="245" x2="935" y2="222" stroke="var(--navy)" stroke-width="4"/>
      <line x1="868" y1="272" x2="1515" y2="245" stroke="var(--navy)" stroke-width="4"/>
      <line x1="1455" y1="100" x2="1795" y2="85" stroke="var(--orange)" stroke-width="4"/>
    </svg>

    <div class="brand">
      <div class="brand-mark"></div>
      <div class="brand-name">TAMLIN</div>
      <div class="brand-sub">ASPHALT &amp; CONCRETE</div>
    </div>

    <div class="headline">
      <p class="tagline">RENDERS BEST SERVICES FOR YOUR</p>
      <h1 class="title">ASPHALT &amp; CONCRETE <span class="accent">NEEDS</span></h1>
    </div>

    <ul class="services col-1">
      <li><svg class="tick" viewBox="0 0 10 10"><rect x="0.5" y="0.5" width="9" height="9" fill="none" stroke="var(--cyan)"/><path d="M2 5 L4.2 7 L8.5 2" fill="none" stroke="var(--cyan)" stroke-width="1.5"/></svg>CONCRETE DRIVEWAYS</li>
      <li><svg class="tick" viewBox="0 0 10 10"><rect x="0.5" y="0.5" width="9" height="9" fill="none" stroke="var(--cyan)"/><path d="M2 5 L4.2 7 L8.5 2" fill="none" stroke="var(--cyan)" stroke-width="1.5"/></svg>CONCRETE APRONS</li>
      <li><svg class="tick" viewBox="0 0 10 10"><rect x="0.5" y="0.5" width="9" height="9" fill="none" stroke="var(--cyan)"/><path d="M2 5 L4.2 7 L8.5 2" fill="none" stroke="var(--cyan)" stroke-width="1.5"/></svg>CONCRETE SIDEWALK</li>
    </ul>
    <ul class="services col-2">
      <li><svg class="tick" viewBox="0 0 10 10"><rect x="0.5" y="0.5" width="9" height="9" fill="none" stroke="var(--cyan)"/><path d="M2 5 L4.2 7 L8.5 2" fill="none" stroke="var(--cyan)" stroke-width="1.5"/></svg>CONCRETE PATIOS</li>
      <li><svg class="tick" viewBox="0 0 10 10"><rect x="0.5" y="0.5" width="9" height="9" fill="none" stroke="var(--cyan)"/><path d="M2 5 L4.2 7 L8.5 2" fill="none" stroke="var(--cyan)" stroke-width="1.5"/></svg>STEPS &amp; STOOPS</li>
      <li><svg class="tick" viewBox="0 0 10 10"><rect x="0.5" y="0.5" width="9" height="9" fill="none" stroke="var(--cyan)"/><path d="M2 5 L4.2 7 L8.5 2" fill="none" stroke="var(--cyan)" stroke-width="1.5"/></svg>GARAGE FLOORS</li>
    </ul>
    <ul class="services col-3">
      <li><svg class="tick" viewBox="0 0 10 10"><rect x="0.5" y="0.5" width="9" height="9" fill="none" stroke="var(--cyan)"/><path d="M2 5 L4.2 7 L8.5 2" fill="none" stroke="var(--cyan)" stroke-width="1.5"/></svg>ASPHALT DRIVEWAYS</li>
      <li><svg class="tick" viewBox="0 0 10 10"><rect x="0.5" y="0.5" width="9" height="9" fill="none" stroke="var(--cyan)"/><path d="M2 5 L4.2 7 L8.5 2" fill="none" stroke="var(--cyan)" stroke-width="1.5"/></svg>ASPHALT SEALCOATING</li>
      <li><svg class="tick" viewBox="0 0 10 10"><rect x="0.5" y="0.5" width="9" height="9" fill="none" stroke="var(--cyan)"/><path d="M2 5 L4.2 7 L8.5 2" fill="none" stroke="var(--cyan)" stroke-width="1.5"/></svg>ASPHALT ADDITIONS</li>
    </ul>

    <div class="contact">
      <p class="contact-label">you can always contact us</p>
      <div class="contact-row">
        <svg class="icon" viewBox="0 0 16 16"><circle cx="8" cy="8" r="8" fill="var(--navy)"/><path d="M5.5 4.5 L7 4.3 L7.6 6.3 L6.7 7 C7.2 8.2 7.9 8.9 9 9.4 L9.8 8.5 L11.7 9.1 L11.5 10.6 C8 11 5 8 5.5 4.5 Z" fill="var(--white)"/></svg>
        <span class="phone">612-555-0148</span>
      </div>
      <div class="contact-row">
        <svg class="icon" viewBox="0 0 16 16"><circle cx="8" cy="8" r="8" fill="var(--orange)"/><circle cx="8" cy="8" r="4" fill="none" stroke="var(--white)" stroke-width="1"/><line x1="4" y1="8" x2="12" y2="8" stroke="var(--white)" stroke-width="1"/><ellipse cx="8" cy="8" rx="1.8" ry="4" fill="none" stroke="var(--white)" stroke-width="1"/></svg>
        <span class="web">tamlin-paving.com</span>
      </div>
    </div>

    <div class="partners" aria-label="Partner and accreditation badges">
      <span class="badge listing"></span>
      <span class="badge association"></span>
      <span class="badge institute"></span>
      <span class="badge rating"></span>
      <span class="badge review"></span>
    </div>
  </div>
</body>
</html>
```